Corbett Architecture (business card)

We need a business card design. We are a full service architectural firm that specializes in mostly residential projects and some commercial projects. We are located in Hudson Valley, New York. We work with high end clients and want a business card that is memorable and has a sleek, modern, design but will not go out of style (timeless).

Target Market(s)

high end residential clients

Industry/Entity Type

Architect

Contact Information for Business Card

Front of card
Company Logo
website: www.corbettdesignstudo.example
what we do: residential, Commercial

back of card
Owner's Name: Martin Corbett
owner's title: Principal
Business address: 2867 Orchard Lane Suite B, Maplethorpe, NY 10938
phone number: 845-555-0192
e-mail: mc@corbettdesignstudio.example

We like:
icons
sleek and clean design
simple not too busy or too much text

Font styles to use
Sans Serif

Colors
0356a4

Requirements
Must have
• company colors are navy blue, white, and gray
• Front of card
• Company Logo
• website: www.corbettdesignstudo.example
• what we do: residential, Commercial
• back of card
• Owner's Name: Martin Corbett
• owner's title: Principal
• Business address: 2867 Orchard Lane Suite B, Maplethorpe, NY 10938
• phone number: 845-555-0192
• e-mail: mc@corbettdesignstudio.example
Nice to have
• We like:
• icons
• sleek and clean design
• simple not too much text
• color of the card to be either blue or gray
Should not have
• we do not like houses in the design or plans of houses-this is over done and we don't like it.
• no QR CODES

```html
<!DOCTYPE html>
<html lang="en">
<head>
<meta charset="utf-8">
<title>Corbett Architecture — Business Card</title>
<link href="https://fonts.googleapis.com/css2?family=Jost:wght@400;500&family=Oswald:wght@300&family=PT+Sans&display=swap" rel="stylesheet">
<style>
  :root {
    --navy: #25226a;
    --band-gray: #7f8180;
    --stage: #676767;
    --white: #ffffff;
    --ink: #111111;
    --text-gray: #444444;
  }
  * { margin: 0; padding: 0; box-sizing: border-box; }
  html, body { width: 1200px; height: 1200px; overflow: hidden; background: var(--stage); }
  .card { position: absolute; left: 111px; width: 930px; height: 531px; overflow: hidden; box-shadow: 6px 8px 14px rgba(0,0,0,0.35); }

  /* Front */
  .card-front { top: 34px; background: var(--navy); }
  .brand { position: absolute; left: 292px; top: 206px; display: flex; align-items: center; gap: 22px; color: var(--white); font-family: "Jost", sans-serif; font-weight: 400; }
  .brand-square { width: 18px; height: 112px; background: var(--white); }
  .brand-name { font-size: 52px; line-height: 1.05; letter-spacing: 1px; text-transform: uppercase; }
  .website { position: absolute; left: 0; right: 0; top: 458px; text-align: center; color: var(--white); font-family: "Jost", sans-serif; font-size: 29px; letter-spacing: 0.5px; }
  .services-band { position: absolute; left: 0; right: 0; bottom: 0; height: 37px; background: var(--band-gray); color: var(--ink); font-family: "PT Sans", sans-serif; font-size: 22px; text-align: center; line-height: 37px; letter-spacing: 0.8px; }

  /* Back */
  .card-back { top: 595px; background: var(--white); }
  .back-panel { position: absolute; left: 0; top: 0; width: 254px; height: 100%; background: var(--navy); display: flex; align-items: center; justify-content: center; }
  .back-panel-name { color: var(--white); font-family: "Jost", sans-serif; font-weight: 400; font-size: 30px; line-height: 1.15; text-align: center; text-transform: uppercase; letter-spacing: 1px; }
  .back-stripe { position: absolute; left: 254px; top: 0; width: 85px; height: 100%; background: var(--band-gray); }
  .owner { position: absolute; left: 465px; top: 85px; color: var(--text-gray); font-family: "Jost", sans-serif; font-weight: 500; }
  .owner-name { font-size: 33px; letter-spacing: 0.5px; text-transform: uppercase; line-height: 1.1; }
  .owner-title { font-size: 21px; margin-top: 6px; margin-left: 2px; text-transform: uppercase; }
  .contacts { position: absolute; left: 470px; top: 282px; list-style: none; color: var(--text-gray); font-family: "Oswald", sans-serif; font-weight: 300; font-size: 20px; }
  .contacts li { display: flex; align-items: center; height: 26px; margin-bottom: 27px; }
  .contacts svg { width: 26px; height: 26px; margin-right: 17px; fill: var(--text-gray); }
</style>
</head>
<body>
  <section class="card card-front">
    <div class="brand">
      <div class="brand-square"></div>
      <div class="brand-name">Corbett<br>Architecture</div>
    </div>
    <p class="website">www.corbettdesignstudo.example</p>
    <p class="services-band">We do Residential and commercial projects</p>
  </section>

  <section class="card card-back">
    <div class="back-panel"><p class="back-panel-name">Corbett<br>Architecture</p></div>
    <div class="back-stripe"></div>
    <div class="owner">
      <h1 class="owner-name">Martin Corbett</h1>
      <p class="owner-title">Principal</p>
    </div>
    <ul class="contacts">
      <li>
        <svg viewBox="0 0 24 24" aria-hidden="true"><path d="M6.6 10.8a15.1 15.1 0 0 0 6.6 6.6l2.2-2.2c.3-.3.7-.4 1-.2 1.1.4 2.3.6 3.6.6.6 0 1 .4 1 1V20c0 .6-.4 1-1 1A17 17 0 0 1 3 4c0-.6.4-1 1-1h3.5c.6 0 1 .4 1 1 0 1.3.2 2.5.6 3.6.1.3 0 .7-.2 1z"/></svg>
        <span>845-555-0192</span>
      </li>
      <li>
        <svg viewBox="0 0 24 24" aria-hidden="true"><path d="M2 5h20v14H2zm1.5 1.5v.3l8.5 6.3 8.5-6.3v-.3zm0 2.2v8.1l5.2-4.2zm17 0-5.2 3.9 5.2 4.2zM9.9 13.6l-5.7 4h15.6l-5.7-4-2.1 1.6z"/></svg>
        <span>mc@corbettdesignstudio.example</span>
      </li>
      <li>
        <svg viewBox="0 0 24 24" aria-hidden="true"><path d="M12 1a7 7 0 0 0-7 7c0 5 7 15 7 15s7-10 7-15a7 7 0 0 0-7-7zm0 10a3 3 0 1 1 0-6 3 3 0 0 1 0 6z"/></svg>
        <span>2867 Orchard Lane Suite B, Maplethorpe, NY 10938</span>
      </li>
    </ul>
  </section>
</body>
</html>
```